Banner Designs for Drone Defense Ad Campaign

Corvane is a security consulting and services company that offers a service called SkyMindful. SkyMindful helps our customers identify security risks from drones and develops comprehensive protection programs. We are looking for a designer to create a banner ad in three sizes for our campaign.
Target Market(s)
Our campaign is geared to the sports and entertainment industry, specifically large event venues and their security operation.
Industry/Entity Type
Security
Font styles to use
Other font styles liked:
- Raleway
Requirements
Must have
- Banner Objective
The visual and textual content of the banner should prompt the viewer to quickly identify the service offered and the information that is available to download.
Banner Design
Logo: SkyMindful logo
Call to Action Button in Red: Get It Here (On Right or or Upper Right)
Title in Larger Font: Guide to UAS Risk Mitigation
Subtitle in smaller Font: 5 Steps to Develop Your Comprehensive UAS Defense Program
Background: Stadium with a drone flying in foreground
Font: Raleway
Banner Sizes
1 - 1200x670 pixels
2 - 1510x196 pixels
3 - 1200x628 pixels

```html
<!DOCTYPE html>
<html lang="en">
<head>
<meta charset="utf-8">
<title>SkyMindful by Corvane – UAS Risk Mitigation Banners</title>
<link href="https://fonts.googleapis.com/css2?family=Raleway:wght@400;500;700;800&family=Roboto:ital,wght@1,900&display=swap" rel="stylesheet">
<style>
  :root {
    --board-light: #f2f2f2;
    --board-mid: #d6d6d6;
    --board-dark: #9d9d9d;
    --brand-blue: #2f6db5;
    --band-blue: #3a78c0;
    --deep-blue: #245a9c;
    --sky-white: #ffffff;
    --ink: #1c1c1c;
    --muted-ink: #3d3d3d;
    --cta-red: #e0141a;
    --cta-red-dark: #b50d12;
    --stadium-light: #d6ecf3;
    --stadium-mid: #7fb8cf;
    --stadium-deep: #2f7fa3;
    --drone-tone: #e9eef3;
    --drone-shade: #b8c4cf;
  }
  * { box-sizing: border-box; margin: 0; padding: 0; }
  html, body { width: 1200px; height: 1200px; overflow: hidden; }
  body {
    position: relative;
    font-family: "Raleway", Arial, sans-serif;
    background: linear-gradient(100deg, var(--board-dark) 0%, var(--board-mid) 45%, var(--board-light) 100%);
  }

  .banner {
    position: absolute;
    overflow: hidden;
    background: linear-gradient(180deg, var(--sky-white) 0%, #eef3f9 35%, #9fbfe2 62%, var(--band-blue) 100%);
    box-shadow: 0 2px 6px rgba(0,0,0,0.18);
  }
  .banner--large { left: 194px; top: 38px; width: 834px; height: 463px; }
  .banner--wide { left: 88px; top: 540px; width: 1049px; height: 136px; }
  .banner--medium { left: 190px; top: 720px; width: 833px; height: 434px; }

  .stadium-photo {
    position: absolute;
    background: radial-gradient(ellipse at 30% 15%, var(--sky-white) 0%, var(--stadium-light) 25%, var(--stadium-mid) 60%, var(--stadium-deep) 100%);
  }
  .banner--large .stadium-photo { left: 270px; top: 0; width: 564px; height: 358px; border-top-left-radius: 320px 300px; }
  .banner--medium .stadium-photo { left: 270px; top: 0; width: 563px; height: 338px; border-top-left-radius: 320px 290px; }
  .banner--wide .stadium-photo { left: 664px; top: 0; width: 385px; height: 136px; border-top-left-radius: 60px 136px; }

  .venue-arc { position: absolute; pointer-events: none; }

  .drone-photo {
    position: absolute;
    border-radius: 40px 40px 24px 24px;
    background: radial-gradient(ellipse at 50% 40%, var(--sky-white) 0%, var(--drone-tone) 45%, var(--drone-shade) 100%);
    opacity: 0.95;
  }
  .banner--large .drone-photo { left: 13px; top: 169px; width: 355px; height: 164px; }
  .banner--medium .drone-photo { left: 8px; top: 162px; width: 355px; height: 164px; }
  .banner--wide .drone-photo { left: 562px; top: 16px; width: 176px; height: 92px; border-radius: 22px 22px 14px 14px; }

  .brand { position: absolute; text-align: right; color: var(--brand-blue); }
  .brand__name { display: block; font-weight: 500; line-height: 1; }
  .brand__by { display: block; font-weight: 500; color: var(--muted-ink); line-height: 1; }
  .banner--large .brand { left: 57px; top: 52px; }
  .banner--large .brand__name { font-size: 37px; }
  .banner--large .brand__by { font-size: 21px; margin-top: 8px; }
  .banner--medium .brand { left: 55px; top: 48px; }
  .banner--medium .brand__name { font-size: 37px; }
  .banner--medium .brand__by { font-size: 21px; margin-top: 8px; }

  .cta {
    position: absolute;
    display: flex;
    align-items: center;
    justify-content: center;
    gap: 12px;
    background: linear-gradient(180deg, var(--cta-red) 0%, var(--cta-red-dark) 100%);
    border: 2px solid var(--sky-white);
    border-radius: 5px;
    color: var(--sky-white);
    font-family: "Roboto", Arial, sans-serif;
    font-style: italic;
    font-weight: 900;
    text-transform: uppercase;
    letter-spacing: 0.5px;
    box-shadow: 0 2px 4px rgba(0,0,0,0.25);
  }
  .cta__icon { fill: var(--sky-white); }
  .banner--large .cta { left: 515px; top: 14px; width: 298px; height: 47px; font-size: 30px; }
  .banner--medium .cta { left: 516px; top: 13px; width: 296px; height: 45px; font-size: 30px; }
  .banner--wide .cta { left: 837px; top: 9px; width: 200px; height: 30px; font-size: 19px; gap: 7px; }

  .title-band {
    position: absolute;
    left: 0;
    width: 100%;
    display: flex;
    align-items: center;
    justify-content: center;
    background: var(--sky-white);
    font-size: 43px;
    line-height: 1;
    color: var(--ink);
    letter-spacing: 0.3px;
  }
  .title-band__lead { font-weight: 400; margin-right: 12px; }
  .title-band__focus { font-weight: 700; color: var(--brand-blue); }
  .banner--large .title-band { top: 358px; height: 60px; }
  .banner--medium .title-band { top: 338px; height: 60px; }

  .subtitle-band {
    position: absolute;
    left: 0;
    width: 100%;
    display: flex;
    align-items: center;
    justify-content: center;
    gap: 14px;
    background: var(--band-blue);
    color: var(--sky-white);
    font-size: 19px;
    font-weight: 500;
    text-transform: uppercase;
  }
  .subtitle-band__rule { width: 42px; height: 2px; background: var(--sky-white); }
  .banner--large .subtitle-band { top: 420px; height: 43px; }
  .banner--medium .subtitle-band { top: 400px; height: 34px; }

  /* Wide leaderboard */
  .banner--wide { background: linear-gradient(90deg, #dfe9f5 0%, #8fb3dc 45%, var(--band-blue) 100%); }
  .brand-panel {
    position: absolute;
    left: 0; top: 0;
    width: 175px; height: 136px;
    background: linear-gradient(180deg, var(--sky-white), #f1f1f1);
    border-top-right-radius: 120px 136px;
  }
  .banner--wide .brand { left: 24px; top: 58px; }
  .banner--wide .brand__name { font-size: 21px; }
  .banner--wide .brand__by { font-size: 12px; margin-top: 4px; }
  .wide-heading { position: absolute; left: 211px; top: 22px; color: var(--sky-white); line-height: 1; z-index: 2; }
  .wide-heading__lead { display: block; font-size: 30px; font-weight: 400; color: var(--ink); }
  .wide-heading__focus { display: block; font-size: 31px; font-weight: 700; margin-top: 5px; }
  .wide-subtitle {
    position: absolute;
    left: 205px; top: 109px;
    width: 432px; height: 22px;
    padding-left: 8px;
    display: flex; align-items: center;
    background: var(--deep-blue);
    color: var(--sky-white);
    font-size: 11px;
    font-weight: 500;
    text-transform: uppercase;
    white-space: nowrap;
  }
</style>
</head>
<body>

  <section class="banner banner--large" aria-label="SkyMindful banner 1200 by 670">
    <div class="stadium-photo" role="img" aria-label="Photo of a large open-roof sports stadium with blue seating"></div>
    <svg class="venue-arc" width="834" height="358" viewBox="0 0 834 358" aria-hidden="true">
      <path d="M250 358 C255 200 300 60 420 0" fill="none" stroke="#3a78c0" stroke-width="22" opacity="0.9"/>
    </svg>
    <div class="drone-photo" role="img" aria-label="Photo of a white quadcopter drone with camera hovering in the foreground"></div>
    <div class="brand">
      <span class="brand__name">SkyMindful</span>
      <span class="brand__by">By Corvane</span>
    </div>
    <a class="cta">
      <svg class="cta__icon" width="22" height="24" viewBox="0 0 22 24" aria-hidden="true"><path d="M0 0 L22 12 L0 24 Z"/></svg>
      Get it here!
    </a>
    <h2 class="title-band"><span class="title-band__lead">GUIDE TO</span><span class="title-band__focus">UAS RISK MITIGATION</span></h2>
    <p class="subtitle-band"><span class="subtitle-band__rule"></span>5 Steps to Develop Your Comprehensive UAS Defense Program<span class="subtitle-band__rule"></span></p>
  </section>

  <section class="banner banner--wide" aria-label="SkyMindful banner 1510 by 196">
    <div class="stadium-photo" role="img" aria-label="Photo of a large open-roof sports stadium with blue seating"></div>
    <svg class="venue-arc" width="1049" height="136" viewBox="0 0 1049 136" aria-hidden="true">
      <path d="M650 136 C660 80 680 30 730 0" fill="none" stroke="#3a78c0" stroke-width="12" opacity="0.9"/>
    </svg>
    <div class="drone-photo" role="img" aria-label="Photo of a white quadcopter drone with camera"></div>
    <div class="brand-panel"></div>
    <div class="brand">
      <span class="brand__name">SkyMindful</span>
      <span class="brand__by">By Corvane</span>
    </div>
    <h2 class="wide-heading"><span class="wide-heading__lead">GUIDE TO</span><span class="wide-heading__focus">UAS RISK MITIGATION</span></h2>
    <p class="wide-subtitle">5 Steps to Develop Your Comprehensive UAS Defense Program</p>
    <a class="cta">
      <svg class="cta__icon" width="14" height="16" viewBox="0 0 22 24" aria-hidden="true"><path d="M0 0 L22 12 L0 24 Z"/></svg>
      Get it here!
    </a>
  </section>

  <section class="banner banner--medium" aria-label="SkyMindful banner 1200 by 628">
    <div class="stadium-photo" role="img" aria-label="Photo of a large open-roof sports stadium with blue seating"></div>
    <svg class="venue-arc" width="833" height="338" viewBox="0 0 833 338" aria-hidden="true">
      <path d="M250 338 C255 190 300 60 420 0" fill="none" stroke="#3a78c0" stroke-width="22" opacity="0.9"/>
    </svg>
    <div class="drone-photo" role="img" aria-label="Photo of a white quadcopter drone with camera hovering in the foreground"></div>
    <div class="brand">
      <span class="brand__name">SkyMindful</span>
      <span class="brand__by">By Corvane</span>
    </div>
    <a class="cta">
      <svg class="cta__icon" width="22" height="24" viewBox="0 0 22 24" aria-hidden="true"><path d="M0 0 L22 12 L0 24 Z"/></svg>
      Get it here!
    </a>
    <h2 class="title-band"><span class="title-band__lead">GUIDE TO</span><span class="title-band__focus">UAS RISK MITIGATION</span></h2>
    <p class="subtitle-band">5 Steps to Develop Your Comprehensive UAS Defense Program</p>
  </section>

</body>
</html>
```